Events company needs professional workshop flyer design

We need a flyer design to advertise a workshop we are holding. The workshop is for professionals (Speech Pathologists, teachers, Psychologists).

I have attached a flyer with all the information in it. We need the flyer to look modern, and attract the attention of teachers to read it, to encourage them to attend a course to further their knowledge and skills.

It needs to list (as per flyer attached):
- The title of the workshop "Bright Horizons Forward:Growing Voices Together Always. Listen - Build - Rise
- Presented by Professor Maren Holt-Avery (Speech & Language Therapist) & Professor Samuel Pryce (Developmental Psychologist)
- The 4 separate locations it is being held (with dates, and addresses)
- A section for intro of "expert speakers...etc"
- A section for topics to be covered
- A section for learning outcomes of the workshop
- Price
- Registration methods
- Who should attend the workshop
- Bio's of both speakers

It needs to be an A4 vertical brochure that is double sided.

```html
<!DOCTYPE html>
<html lang="en">
<head>
<meta charset="utf-8">
<title>About the Presenters – Workshop Flyer</title>
<link href="https://fonts.googleapis.com/css2?family=PT+Sans:wght@400;700&display=swap" rel="stylesheet">
<style>
  :root {
    --frame: #d3cfc4;
    --paper: #e9e7dc;
    --rose: #b85b73;
    --rose-text: #f6eef0;
    --slate: #466a88;
    --slate-text: #eef1f3;
    --ink-blue: #3f6585;
    --photo-frame: #c9c5ba;
  }
  html, body {
    margin: 0;
    padding: 0;
    width: 849px;
    height: 1200px;
    overflow: hidden;
    background: var(--frame);
    font-family: "PT Sans", "Myriad Pro", Arial, sans-serif;
  }
  .flyer {
    position: relative;
    width: 849px;
    height: 1200px;
  }
  .sheet {
    position: absolute;
    left: 12px; top: 12px; right: 12px; bottom: 12px;
    background: var(--paper);
  }
  .about-band {
    position: absolute;
    left: 89px; top: 145px;
    width: 671px; height: 111px;
    background: var(--rose);
    color: var(--rose-text);
    text-align: center;
  }
  .about-band h1 {
    margin: 14px 0 6px;
    font-size: 31px;
    line-height: 36px;
    font-weight: 700;
    letter-spacing: 0.5px;
  }
  .about-band .presenters {
    margin: 0;
    font-size: 16px;
    line-height: 20px;
    font-weight: 700;
  }
  .about-band .workshop-title {
    margin: 2px 0 0;
    font-size: 16px;
    line-height: 20px;
  }
  .portrait {
    position: absolute;
    top: 303px;
    width: 136px; height: 149px;
    margin: 0;
    background: var(--photo-frame);
  }
  .portrait .photo {
    position: absolute;
    left: 7px; top: 7px; right: 7px; bottom: 7px;
    background: linear-gradient(160deg, #b5b5b5, #5d5d5d);
  }
  .portrait--maren { left: 279px; }
  .portrait--samuel { left: 435px; }
  .portrait--samuel .photo { background: linear-gradient(160deg, #f2f2f2, #9a9a9a); }
  .bio {
    position: absolute;
    top: 467px;
    width: 218px;
    margin: 0;
    font-size: 11.4px;
    line-height: 14.4px;
    color: var(--ink-blue);
    text-align: justify;
  }
  .bio--maren { left: 192px; }
  .bio--samuel { left: 438px; }
  .info-panel {
    position: absolute;
    left: 89px; top: 750px;
    width: 671px; height: 302px;
    background: var(--slate);
    color: var(--slate-text);
  }
  .cost {
    position: absolute;
    left: 76px; top: 62px;
    width: 170px;
    text-align: center;
    font-size: 15.5px;
    line-height: 19px;
  }
  .cost h2 {
    margin: 0 0 10px;
    font-size: 24px;
    line-height: 28px;
  }
  .cost p { margin: 0; }
  .divider {
    position: absolute;
    left: 247px; top: 30px;
    width: 1px; height: 250px;
    background: var(--slate-text);
  }
  .register {
    position: absolute;
    left: 265px; top: 20px;
    width: 396px;
    font-size: 16px;
    line-height: 21px;
  }
  .register h2 {
    margin: 0 0 8px;
    font-size: 24px;
    line-height: 28px;
  }
  .register p { margin: 0; }
  .register .web { font-weight: 700; }
  .register .audience { width: 340px; }
  .rule {
    height: 1px;
    width: 381px;
    margin: 15px 0 11px;
    background: var(--slate-text);
  }
  .cancellation {
    position: absolute;
    left: 89px; top: 1059px;
    width: 671px;
    margin: 0;
    font-size: 11.8px;
    line-height: 17.4px;
    color: var(--ink-blue);
    text-align: justify;
  }
  .cancellation strong { font-size: 13px; }
</style>
</head>
<body>
<main class="flyer">
  <div class="sheet"></div>

  <header class="about-band">
    <h1>ABOUT</h1>
    <p class="presenters">Professor Maren Holt-Avery &amp; Professor Samuel Pryce</p>
    <p class="workshop-title">Bright Horizons Forward: Growing Voices Together Always</p>
  </header>

  <figure class="portrait portrait--maren">
    <div class="photo" role="img" aria-label="Portrait photograph of Professor Maren Holt-Avery"></div>
  </figure>
  <figure class="portrait portrait--samuel">
    <div class="photo" role="img" aria-label="Portrait photograph of Professor Samuel Pryce"></div>
  </figure>

  <p class="bio bio--maren">Maren is Professor of Child Language and Learning at the University of Northbridge, UK. She is the director of a nationwide longitudinal study on specific language impairment (SLI) that has been following individuals from 7 years of age to adult life. Maren has an interest in the interface between clinical practice and research. She is founder member of the SPEAK UP campaign to raise awareness of SLI (www.speakupcampaign.org), was editor of the Journal of Child Communication Studies and was involved in the development of national clinical guidelines for language disorders in children.</p>

  <p class="bio bio--samuel">Samuel Pryce is Professor of Psychology at the University of Glenmoor, UK. He has previously held a Chair at the University of Westhaven and was Director of the Westhaven Child Development Centre. He has a long established interest in language difficulties and child development. He has written a large number of journal articles and books for academics and practitioners, and is editor of the journal Early Words Review. For the past ten years he has been co-directing the longitudinal study of SLI with Maren Holt-Avery.</p>

  <section class="info-panel">
    <div class="cost">
      <h2>COST</h2>
      <p>2 days: <strong>$495</strong> (Earlybird)<br>Add an additional <strong>$88</strong> if registering within 3 weeks of workshop.<br>(incl G.S.T, workshop materials, morning and afternoon tea, lunch)</p>
    </div>
    <div class="divider"></div>
    <div class="register">
      <h2>TO REGISTER</h2>
      <p>Register online at:<br><span class="web">http://www.brightvoicesspeech.com.au/</span><br>events/ or Call Clara Benning on 02 4000 1234 or email events@brightvoicesspeech.com.au for invoicing for your school or workplace</p>
      <div class="rule"></div>
      <h2>Who should attend</h2>
      <p class="audience">For Teachers, Speech Pathologists, Psychologists and those interested in learning more about children with Language Learning difficulties</p>
    </div>
  </section>

  <p class="cancellation"><strong>Cancellation Policy</strong>: In the event that a participant cancels, The registration fee minus a 10% processing fee ($49.50) will be refunded until Thursday 22nd January 2015. After this date, there will be no refund. If the hosts cancel (Bright Voices Speech Pathology), or defers the event, 100% of the registration fee will be refunded if the registrant cannot attend on the revised dates, however the hosts bear no responsibility for any costs incurred (such as flights, accommodation, travel expenses) or loss of income.</p>
</main>
</body>
</html>
```